Business Card

Just need business logo with phone number on it. 0472 318 506
And the following on the bottom of the card.

"Your local plumbing experts".
and emblems for kovo card, cheque and cash

```html
<!DOCTYPE html>
<html lang="en">
<head>
<meta charset="utf-8">
<title>Ridgeline Plumbing &amp; Drainage – Business Card</title>
<link rel="stylesheet" href="https://fonts.googleapis.com/css2?family=Open+Sans:ital,wght@0,400;0,600;0,700;1,400&display=swap">
<style>
  :root {
    --brand-red: #e8202a;
    --brand-blue: #1a8fd6;
    --text-grey: #4f5357;
    --card-white: #ffffff;
    --backdrop: #ece8e3;
  }
  * { box-sizing: border-box; margin: 0; padding: 0; }
  html, body {
    width: 1200px;
    height: 1000px;
    overflow: hidden;
    background: var(--backdrop);
    font-family: "Open Sans", sans-serif;
  }
  .business-card {
    position: absolute;
    left: 100px;
    top: 201px;
    width: 1000px;
    height: 598px;
    background: var(--card-white);
    box-shadow: 0 6px 18px rgba(0, 0, 0, 0.18);
    text-align: center;
    color: var(--text-grey);
  }
  .brand {
    position: absolute;
    top: 118px;
    left: 0;
    width: 100%;
    display: flex;
    justify-content: center;
    align-items: center;
    gap: 22px;
  }
  .brand-dot {
    width: 30px;
    height: 30px;
    border-radius: 50%;
    background: var(--brand-blue);
    flex: none;
  }
  .brand-name {
    color: var(--brand-red);
    font-weight: 700;
    font-size: 52px;
    line-height: 1.1;
    letter-spacing: 1px;
    text-transform: uppercase;
    text-align: left;
  }
  .brand-name .line-two { display: block; font-size: 52px; }
  .contact {
    position: absolute;
    top: 320px;
    left: 0;
    width: 100%;
  }
  .contact-name {
    color: var(--brand-red);
    font-weight: 700;
    font-size: 31px;
    line-height: 1;
    margin-bottom: 22px;
  }
  .contact-line {
    font-size: 24px;
    line-height: 33px;
  }
  .tagline {
    font-weight: 700;
    font-size: 24px;
    line-height: 33px;
    margin-top: 17px;
  }
  .payment-note {
    font-size: 24px;
    line-height: 33px;
  }
</style>
</head>
<body>
  <main class="business-card">
    <div class="brand">
      <span class="brand-dot" aria-hidden="true"></span>
      <div class="brand-name">Ridgeline<span class="line-two">Plumbing &amp; Drainage</span></div>
    </div>
    <section class="contact">
      <p class="contact-name">DALE HARTIGAN</p>
      <p class="contact-line">0472 318 506</p>
      <p class="contact-line">hello@ridgelineplumbing.com.au</p>
      <p class="tagline">“Your local plumbing experts"</p>
      <p class="payment-note">Emblems for kovo card, cheque and cash</p>
    </section>
  </main>
</body>
</html>
```